Stationary Design Letterhead and Envelope

Artist should provide Letterhead and envelop stationary designs

Info for stationary:
Fernhallow Outdoor Advertising
4873 Quarry Rd. 915 N. PO BOX 528617
Austin, TX 78519

Dale Fernhallow
President
555-862-1907
dale@fernhallowsigns.example
fernhallowsigns.example

Target Market(s)

clients

Colors
0054AA
0677BA
7BADD7
CADEEF
E8F1F8

Requirements
Must have
• high quality unique eye catching and dynamic

```html
<!DOCTYPE html>
<html lang="en">
<head>
<meta charset="utf-8">
<title>Fernhallow Outdoor Advertising – Letterhead and Envelope</title>
<link rel="stylesheet" href="https://fonts.googleapis.com/css2?family=Mulish:wght@400;600;700;800&family=Dancing+Script:wght@500&display=swap">
<style>
  :root {
    --backdrop: #d4d4d4;
    --paper: #f7f7f7;
    --brand-blue: #0f6ca8;
    --accent-blue: #0677BA;
    --ink: #2b2b2b;
    --ink-dark: #111111;
    --fold-line: #c9c9c9;
  }
  * { margin: 0; padding: 0; box-sizing: border-box; }
  html, body { width: 1200px; height: 971px; overflow: hidden; }
  body {
    background: var(--backdrop);
    font-family: "Mulish", sans-serif;
    color: var(--ink);
    position: relative;
  }
  .sheet {
    position: absolute;
    background: var(--paper);
    overflow: hidden;
  }
  .letterhead { left: 89px; top: 87px; width: 505px; height: 686px; }
  .envelope-front { left: 636px; top: 181px; width: 488px; height: 244px; }
  .envelope-back { left: 637px; top: 463px; width: 488px; height: 243px; }

  .brand-name {
    position: absolute;
    font-family: "Mulish", sans-serif;
    font-weight: 800;
    color: var(--ink-dark);
    line-height: 1;
    text-align: center;
  }
  .brand-name .brand-word { display: block; font-size: 29px; letter-spacing: 0.5px; }
  .brand-name .brand-line { display: block; font-size: 11.5px; letter-spacing: 0.4px; margin-top: 5px; }
  .letterhead .brand-name { left: 34px; top: 50px; width: 194px; }
  .envelope-front .brand-name { left: 18px; top: 28px; width: 184px; }
  .envelope-front .brand-name .brand-word { font-size: 27.5px; }
  .envelope-front .brand-name .brand-line { font-size: 11px; }

  .contact-block {
    position: absolute;
    left: 323px; top: 32px;
    border-left: 1px solid var(--accent-blue);
    padding-left: 7px;
    font-size: 8px;
    line-height: 11px;
    color: var(--ink-dark);
    height: 90px;
  }
  .contact-name { color: var(--accent-blue); font-weight: 700; font-size: 7.8px; }
  .contact-gap { height: 3px; }
  .contact-row { display: flex; align-items: center; gap: 4px; }
  .contact-row svg { width: 6px; height: 6px; fill: var(--accent-blue); }

  .letter-body {
    position: absolute;
    left: 34px; top: 173px; width: 437px;
    font-size: 9px;
    line-height: 10.7px;
  }
  .letter-date { font-size: 10px; margin-bottom: 12px; }
  .letter-recipient { font-size: 9.3px; line-height: 11.3px; margin-bottom: 11px; }
  .letter-salutation { font-size: 12px; font-weight: 600; margin: 2px 0 11px; }
  .letter-body p.paragraph { text-align: justify; margin-bottom: 10.6px; }
  .letter-closing { margin-top: 23px; font-size: 9.3px; }
  .letter-signature {
    font-family: "Dancing Script", cursive;
    font-size: 22px;
    color: var(--ink-dark);
    margin-top: 12px;
    padding-left: 3px;
  }

  .return-address {
    position: absolute;
    left: 18px; top: 86px;
    font-size: 7.3px;
    line-height: 11px;
    color: var(--ink-dark);
  }

  .wave { position: absolute; left: 0; display: block; }
  .letterhead .wave { top: 596px; width: 505px; height: 90px; }
  .envelope-front .wave { top: 154px; width: 488px; height: 90px; }
  .envelope-back .flap { position: absolute; left: 0; top: 0; width: 488px; height: 243px; }
</style>
</head>
<body>

<section class="sheet letterhead" aria-label="Letterhead">
  <div class="brand-name">
    <span class="brand-word">FERNHALLOW</span>
    <span class="brand-line">OUTDOOR ADVERTISING</span>
  </div>

  <div class="contact-block">
    <div class="contact-name">DALE FERNHALLOW</div>
    <div>President</div>
    <div class="contact-gap"></div>
    <div>Fernhallow Outdoor Advertising</div>
    <div>4873 Quarry Rd. 915 N. PO BOX 528617</div>
    <div>Austin, TX 78519</div>
    <div class="contact-gap"></div>
    <div class="contact-row">
      <svg viewBox="0 0 10 10" aria-hidden="true"><path d="M2 0.5 L4 3 L3 4.2 Q4 6 5.8 7 L7 6 L9.5 8 L8.2 9.5 Q4 9.5 0.5 2 Z"/></svg>
      <span>555-862-1907</span>
    </div>
    <div class="contact-row">
      <svg viewBox="0 0 10 10" aria-hidden="true"><path d="M0 2 H10 V8 H0 Z M0.6 2.5 L5 5.6 L9.4 2.5" fill-rule="evenodd"/></svg>
      <span>dale@fernhallowsigns.example</span>
    </div>
    <div class="contact-row">
      <svg viewBox="0 0 10 10" aria-hidden="true"><circle cx="5" cy="5" r="4.8"/></svg>
      <span>fernhallowsigns.example</span>
    </div>
  </div>

  <div class="letter-body">
    <div class="letter-date">January-03-2020</div>
    <div class="letter-recipient">Mr, Evan Marlow<br>President</div>
    <div class="letter-recipient">Brindle Corporation<br>123 Street Name, Suite# 10<br>City, State, 120023</div>
    <div class="letter-salutation">Dear Mr, Evan</div>
    <p class="paragraph">Lorem ipsum dolor sit amet, consectetur adipisicing elit, sed do eiusmod tempor incididunt ut labore et dolore magna aliqua. Ut enim ad minim veniam, quis nostrud exercitation ullamco laboris nisi ut aliquip ex ea commodo consequat. Duis aute irure dolor in reprehenderit in voluptate velit esse cillum dolore eu fugiat nulla pariatur.</p>
    <p class="paragraph">Lorem ipsum dolor sit amet, consectetur adipisicing elit, sed do eiusmod tempor incididunt ut labore et dolore magna aliqua. Ut enim ad minim veniam, quis nostrud exercitation ullamco laboris nisi ut aliquip ex ea commodo consequat. Duis aute irure dolor in reprehenderit in voluptate velit esse cillum dolore eu fugiat nulla pariatur.</p>
    <p class="paragraph">Lorem ipsum dolor sit amet, consectetur adipisicing elit, sed do eiusmod tempor incididunt ut labore et dolore magna aliqua. Ut enim ad minim veniam, quis nostrud exercitation ullamco laboris nisi ut aliquip ex ea commodo consequat.</p>
    <p class="paragraph">Excepteur sint occaecat cupidatat non proident, sunt in culpa qui officia deserunt mollit anim id est laborum. re et dolore magnam aliquam quaerat voluptatem.</p>
    <div class="letter-closing">Regards</div>
    <div class="letter-signature">Owen Harlan</div>
  </div>

  <svg class="wave" viewBox="0 0 505 90" preserveAspectRatio="none" aria-hidden="true">
    <path d="M0 6 Q252 105 505 0 L505 90 L0 90 Z" fill="var(--brand-blue)"/>
    <path d="M16 7 Q250 88 470 9 Q250 78 16 7 Z" fill="var(--ink-dark)"/>
  </svg>
</section>

<section class="sheet envelope-front" aria-label="Envelope front">
  <div class="brand-name">
    <span class="brand-word">FERNHALLOW</span>
    <span class="brand-line">OUTDOOR ADVERTISING</span>
  </div>
  <div class="return-address">
    Fernhallow Outdoor Advertising<br>
    4873 Quarry Rd. 915 N. PO BOX 528617<br>
    Austin, TX 78519
  </div>
  <svg class="wave" viewBox="0 0 488 90" preserveAspectRatio="none" aria-hidden="true">
    <path d="M0 4 Q244 105 488 7 L488 90 L0 90 Z" fill="var(--brand-blue)"/>
    <path d="M28 9 Q244 89 458 11 Q244 79 28 9 Z" fill="var(--ink-dark)"/>
  </svg>
</section>

<section class="sheet envelope-back" aria-label="Envelope back">
  <svg class="flap" viewBox="0 0 488 243" aria-hidden="true">
    <path d="M14 39 L7 236 L13 242" fill="none" stroke="var(--fold-line)" stroke-width="1"/>
    <path d="M473 39 L481 236 L475 242" fill="none" stroke="var(--fold-line)" stroke-width="1"/>
    <path d="M1 0 C5 28 17 47 35 50 L244 78 L455 47 C473 43 484 20 487 0 Z" fill="var(--brand-blue)"/>
  </svg>
</section>

</body>
</html>
```